New Business Cards for Organic Meat Farm

We need a business card designed for Hollowmere Farm, a meat farm in western MA. Our logo uses a hand-drawn woodcut (attached). Our color palette has been simply black and white (shown in notepad and picture of our food truck). While we are based out of western MA, we have ambitions to grow nationally, so our hope is for a classy and memorable card which will be printed on a premium quality stock from a printer like printkestrel.com.
Target Market(s)
consumers of quality meats, restauranteurs, partnering farms
Industry/Entity Type
Farming and prepared meat products
Contact Information for Business Card
Corwin Aldane, President/Owner, corwin@hollowmerefarm.com, mobile: 413-555-0172, phone: 413-555-0148, hollowmerefarm.com, facebook: @hollowmerefarm, instagram: @thornburyfarmma
Colors
Designer to choose colors to be used in the design.
Look and feel

```html
<!DOCTYPE html>
<html lang="en">
<head>
<meta charset="utf-8">
<title>Hollowmere Farm — Business Card</title>
<link href="https://fonts.googleapis.com/css2?family=Montserrat:wght@500;700&family=Poppins:wght@300;400;500;600&display=swap" rel="stylesheet">
<style>
  :root {
    --stage: #2c2c2d;
    --paper: #ffffff;
    --ink: #2a2a2c;
    --ink-soft: #3a3a3d;
    --muted: #9a9a9e;
    --rule: #e4e4e6;
    --back-top: #2f3030;
    --back-bottom: #3c3d3d;
    --reverse: #ffffff;
  }
  * { margin: 0; padding: 0; box-sizing: border-box; }
  html, body { width: 1200px; height: 1024px; overflow: hidden; }
  body {
    background: var(--stage);
    font-family: "Poppins", sans-serif;
    position: relative;
  }
  .card {
    position: absolute;
    left: 250px;
    width: 700px;
    height: 400px;
    border-radius: 30px;
    overflow: hidden;
  }
  .card-front { top: 82px; background: var(--paper); }
  .card-back {
    top: 542px;
    background: linear-gradient(135deg, var(--back-top) 0%, var(--back-bottom) 55%, var(--back-top) 100%);
  }

  .wordmark {
    font-family: "Poppins", sans-serif;
    font-weight: 600;
    text-align: center;
    line-height: 1.1;
  }
  .wordmark .name { display: block; font-size: 38px; letter-spacing: 0.5px; }
  .wordmark .sub { display: block; font-size: 20px; letter-spacing: 10px; margin-top: 6px; padding-left: 10px; }

  .front-brand {
    position: absolute;
    left: 0; top: 0;
    width: 350px; height: 400px;
    display: flex; flex-direction: column;
    align-items: center; justify-content: center;
    color: var(--ink);
  }
  .brand-dot {
    width: 18px; height: 18px; border-radius: 50%;
    background: currentColor; margin-bottom: 18px;
  }
  .divider {
    position: absolute;
    left: 350px; top: 48px;
    width: 1px; height: 268px;
    background: var(--rule);
  }

  .contact {
    position: absolute;
    left: 385px; top: 70px;
    color: var(--ink);
  }
  .person {
    font-family: "Montserrat", sans-serif;
    font-size: 28px;
    font-weight: 500;
    letter-spacing: 0.5px;
    line-height: 1;
  }
  .person strong { font-weight: 700; }
  .role {
    font-size: 16px;
    font-weight: 300;
    color: var(--muted);
    margin-top: 8px;
  }
  .role-rule {
    width: 64px; height: 2px;
    background: var(--rule);
    margin: 10px 0 18px 10px;
  }
  .contact-list { list-style: none; }
  .contact-list li {
    display: flex; align-items: center;
    gap: 12px;
    font-size: 16px;
    font-weight: 300;
    color: var(--muted);
    height: 32px;
  }
  .icon {
    width: 22px; height: 22px;
    border-radius: 5px;
    background: var(--ink-soft);
    display: flex; align-items: center; justify-content: center;
    flex: none;
  }
  .icon svg { width: 14px; height: 14px; }

  .social-band {
    position: absolute;
    right: 0; bottom: 0;
    width: 320px; height: 48px;
  }
  .social-band svg { position: absolute; inset: 0; }
  .social-row {
    position: absolute;
    right: 26px; bottom: 12px;
    display: flex; align-items: center; gap: 6px;
    color: var(--reverse);
    font-size: 15px;
    font-weight: 400;
  }
  .social-dot {
    width: 20px; height: 20px; border-radius: 50%;
    background: var(--reverse);
  }
  .social-row .handle { margin-left: 4px; }

  .back-brand {
    position: absolute; inset: 0;
    display: flex; flex-direction: column;
    align-items: center; justify-content: center;
    color: var(--reverse);
  }
  .back-brand .wordmark .name { font-size: 46px; }
  .back-brand .wordmark .sub { font-size: 24px; }
</style>
</head>
<body>

<section class="card card-front" aria-label="Business card, front">
  <div class="front-brand">
    <span class="brand-dot"></span>
    <div class="wordmark">
      <span class="name">Hollowmere</span>
      <span class="sub">FARM</span>
    </div>
  </div>

  <div class="divider"></div>

  <div class="contact">
    <h1 class="person">CORWIN <strong>ALDANE</strong></h1>
    <p class="role">President/Owner</p>
    <div class="role-rule"></div>
    <ul class="contact-list">
      <li>
        <span class="icon" aria-hidden="true">
          <svg viewBox="0 0 14 14"><rect x="3.5" y="1" width="7" height="12" rx="1.3" fill="none" stroke="#fff" stroke-width="1.3"/><circle cx="7" cy="10.8" r="0.8" fill="#fff"/></svg>
        </span>
        413-555-0172
      </li>
      <li>
        <span class="icon" aria-hidden="true">
          <svg viewBox="0 0 14 14"><path d="M3 1.5l2.3 2.6-1.2 1.6c.8 1.7 2.2 3.1 3.9 3.9l1.6-1.2 2.6 2.3-1.3 1.8C6 12.2 1.8 8 1.2 2.8z" fill="#fff"/></svg>
        </span>
        413-555-0148
      </li>
      <li>
        <span class="icon" aria-hidden="true">
          <svg viewBox="0 0 14 14"><rect x="1.5" y="3" width="11" height="8" rx="0.8" fill="none" stroke="#fff" stroke-width="1.2"/><path d="M1.8 3.4L7 7.6l5.2-4.2" fill="none" stroke="#fff" stroke-width="1.2"/></svg>
        </span>
        corwin@hollowmerefarm.com
      </li>
      <li>
        <span class="icon" aria-hidden="true">
          <svg viewBox="0 0 14 14"><path d="M3 2l8 4.2-3.4 1 2.3 3.6-1.4.9-2.3-3.6L3.8 10.6z" fill="#fff"/></svg>
        </span>
        hollowmerefarm.com
      </li>
    </ul>
  </div>

  <div class="social-band">
    <svg viewBox="0 0 320 48" preserveAspectRatio="none" aria-hidden="true">
      <polygon points="24,0 320,0 320,48 0,48" fill="var(--ink-soft)"/>
    </svg>
    <div class="social-row">
      <span class="social-dot"></span>
      <span class="social-dot"></span>
      <span class="handle">@hollowmerefarm</span>
    </div>
  </div>
</section>

<section class="card card-back" aria-label="Business card, back">
  <div class="back-brand">
    <span class="brand-dot"></span>
    <div class="wordmark">
      <span class="name">Hollowmere</span>
      <span class="sub">FARM</span>
    </div>
  </div>
</section>

</body>
</html>
```